custom sticker for off the shelf postage packaging

Looking for a custom sticker to wrap around a postage box for gift hampers. Want to avoid custom printing onto the box, and so would like to glam up with a custom sticker. The design needs to be suitable for printing onto a paper sticker (rather than a vinyl sticker) so that the entire box is recyclable. Current marketing material and logo will be provided to the successful applicant. The gift hampers are filled with hand made goodies from places we can't travel to due to Covid. Brand is called TOVA and it stands for Thinking Of Victor Always.

Target Market(s)

Must appear to people who buy stuff on instagram

Industry/Entity Type

Gift Shop

Font styles to use
Other font styles liked:
• syncopate-regular

Requirements
Must have
• Must be eye catching and convey a sense of luxury. The recipient of the box is not the buyer, and won't be familiar with the website, or the brand. So this is a first impression. Draft website can be provided upon request.

Current branding is:
"bg":"#F6E7DC",
"font":"#2B1200",
"icon-gradient-0":"#792300",
"icon-gradient-1":"#F37000",
"slogan":"#3f2614"}
Nice to have
• Sticker should wrap around the box and cover the opening flap for postage security. The box is 310mm x 225mm x 102mm (length x width x height). Thinking that the sticker should be 225mm x 102 x 102mm *so the crease of the sticker should line up with the box. Text should be logo + text down the side "somebody loves you"

```html
<!DOCTYPE html>
<html lang="en">
<head>
<meta charset="utf-8">
<title>TOVA – Wrap-around Box Sticker</title>
<link rel="stylesheet" href="https://fonts.googleapis.com/css2?family=Raleway:wght@300;400&display=swap">
<style>
  :root {
    --bg: #F4E2DA;
    --font: #2B1200;
    --wordmark: #9A2C00;
    --slogan: #3f2614;
    --foliage-a: rgba(160, 138, 130, 0.38);
    --foliage-b: rgba(160, 138, 130, 0.08);
  }
  * { margin: 0; padding: 0; box-sizing: border-box; }
  html, body { width: 1200px; height: 5042px; overflow: hidden; background: var(--bg); }
  .sticker { position: relative; width: 1200px; height: 5042px; background: var(--bg); overflow: hidden; }

  .foliage { position: absolute; }
  .foliage--left { background: linear-gradient(90deg, var(--foliage-a), var(--foliage-b)); border-radius: 0 60% 60% 0; }
  .foliage--right { background: linear-gradient(270deg, var(--foliage-a), var(--foliage-b)); border-radius: 60% 0 0 60%; }
  .foliage--top-left { left: 0; top: 1100px; width: 366px; height: 790px; }
  .foliage--top-right { right: 0; top: 1056px; width: 411px; height: 580px; }
  .foliage--bottom-right { right: 0; top: 2873px; width: 411px; height: 1113px; }
  .foliage--bottom-left { left: 0; top: 3338px; width: 352px; height: 830px; }

  .lockup { position: absolute; left: 0; width: 1200px; color: var(--font); }
  .lockup > * { position: absolute; left: 0; width: 1200px; text-align: center; line-height: 1; white-space: nowrap; }
  .wordmark { font-family: "Raleway", sans-serif; font-weight: 300; color: var(--wordmark); letter-spacing: 0.02em; }
  .slogan { font-family: "Raleway", sans-serif; font-weight: 400; color: var(--slogan); letter-spacing: 0.08em; }
  .heart { left: 50% !important; }

  /* Main lockup */
  .lockup--main { top: 1943px; height: 1130px; }
  .lockup--main .wordmark { top: 0; font-size: 370px; }
  .lockup--main .slogan { font-size: 92px; }
  .lockup--main .slogan--first { top: 508px; }
  .lockup--main .slogan--second { top: 641px; }
  .lockup--main .slogan--third { top: 768px; }
  .lockup--main .heart { top: 945px; width: 190px; height: 175px; margin-left: -95px; }

  /* Small lockups (end panel and flap) */
  .lockup--small { height: 650px; }
  .lockup--small .wordmark { top: 0; font-size: 266px; }
  .lockup--small .slogan { font-size: 64px; }
  .lockup--small .slogan--first { top: 264px; }
  .lockup--small .slogan--second { top: 351px; }
  .lockup--small .slogan--third { top: 441px; }
  .lockup--small .heart { top: 552px; width: 100px; height: 93px; margin-left: -50px; }

  .lockup--end { top: 4096px; }
  .lockup--flap { top: 307px; transform: rotate(180deg) scale(0.92); transform-origin: 600px 325px; }
</style>
</head>
<body>
<main class="sticker">
  <div class="foliage foliage--left foliage--top-left" role="img" aria-label="Line-drawn leafy branch illustration"></div>
  <div class="foliage foliage--right foliage--top-right" role="img" aria-label="Line-drawn leafy branch illustration"></div>
  <div class="foliage foliage--right foliage--bottom-right" role="img" aria-label="Line-drawn leafy branch illustration"></div>
  <div class="foliage foliage--left foliage--bottom-left" role="img" aria-label="Line-drawn leafy branch illustration"></div>

  <section class="lockup lockup--small lockup--flap">
    <span class="wordmark">TOVA</span>
    <span class="slogan slogan--first">somebody</span>
    <span class="slogan slogan--second">loves</span>
    <span class="slogan slogan--third">you</span>
    <svg class="heart" viewBox="0 0 100 92" aria-hidden="true"><path d="M50 86 C20 62 6 48 6 28 C6 14 17 6 29 6 C39 6 46 12 50 20 C54 12 61 6 71 6 C83 6 94 14 94 28 C94 48 80 62 50 86 Z" fill="none" stroke="#2B1200" stroke-width="4" stroke-linejoin="round"/></svg>
  </section>

  <section class="lockup lockup--main">
    <span class="wordmark">TOVA</span>
    <span class="slogan slogan--first">somebody</span>
    <span class="slogan slogan--second">loves</span>
    <span class="slogan slogan--third">you</span>
    <svg class="heart" viewBox="0 0 100 92" aria-hidden="true"><path d="M50 86 C20 62 6 48 6 28 C6 14 17 6 29 6 C39 6 46 12 50 20 C54 12 61 6 71 6 C83 6 94 14 94 28 C94 48 80 62 50 86 Z" fill="none" stroke="#2B1200" stroke-width="3.5" stroke-linejoin="round"/></svg>
  </section>

  <section class="lockup lockup--small lockup--end">
    <span class="wordmark">TOVA</span>
    <span class="slogan slogan--first">somebody</span>
    <span class="slogan slogan--second">loves</span>
    <span class="slogan slogan--third">you</span>
    <svg class="heart" viewBox="0 0 100 92" aria-hidden="true"><path d="M50 86 C20 62 6 48 6 28 C6 14 17 6 29 6 C39 6 46 12 50 20 C54 12 61 6 71 6 C83 6 94 14 94 28 C94 48 80 62 50 86 Z" fill="none" stroke="#2B1200" stroke-width="4" stroke-linejoin="round"/></svg>
  </section>
</main>
</body>
</html>
```